依頼詳細
既存サイトのデザインが古くなったため、リニューアルを行います。
ワイヤーフレーム有。
参考サイト有。
https://www.morisuzu-web.jp/
今風でシンプルなデザインをお願いいたします。
メインカラーは緑で、現在のロゴをお渡ししますので、トレースしSVGで作ってください。
サイトURL
ページ数
1ページ
希望イメージ
シンプル 複雑
単色 カラフル
暗い 明るい
日常 高級
遊び心 厳粛
未来的 伝統的
女性的 男性的
希望する色
緑系
納品ファイル
• イラストレーター形式 (.ai)
補足説明
TOPページ(PC版とスマホ版)のみご提案ください。
採用した場合は、アーカイブと詳細ページ(スタイルガイド)のデザインもお願いいたします。
ワイヤーフレームではなく、サイトマップ有です。
締め切りを10日後に変更しました。
URLの記載があるのは、参考サイトです。
会社名はダミー(株式会社ダミーリサイクル)とし、
添付のサイトマップに合わせて作っていただけると幸いです。
記載内容がややこしくて申し訳ございません。
その他文言等もダミーで結構です。
よろしくお願いいたします。
■ 選んだ理由

シンプルかつ、今風なレイアウトで好感が持てました。

■ 提案者全員のお礼・コメント

修正依頼にも迅速に対応いただき、ありがとうございました。
またご提案よろしくお願いいたします。

```html
<!DOCTYPE html>
<html lang="ja">
<head>
<meta charset="utf-8">
<title>midori-eco</title>
<link rel="stylesheet" href="https://fonts.googleapis.com/css2?family=Noto+Serif+JP:wght@400;700&family=Noto+Sans+JP:wght@400;500;700&display=swap">
<style>
:root{
  --green:#2f6a1f;
  --green-dark:#1f4d14;
  --green-soft:#6f9a3c;
  --ink:#333;
  --line:#d6d6d6;
  --bg-soft:#f3f3f3;
  --white:#fff;
}
*{box-sizing:border-box;margin:0;padding:0}
html,body{width:1200px;height:4784px;overflow:hidden}
body{font-family:"Noto Sans JP",sans-serif;color:var(--ink);background:var(--white);font-size:15px;line-height:1.6;position:relative}
.section{position:absolute;left:0;width:1200px}
.brand{display:flex;align-items:center;gap:12px;font-family:"Noto Serif JP",serif;font-weight:700;color:var(--green);font-size:38px;line-height:1;white-space:nowrap}
.brand-dot{width:40px;height:40px;border-radius:50%;background:var(--green);flex:none}
/* header */
.header{top:0;height:160px}
.header .brand{position:absolute;left:24px;top:30px}
.tel{position:absolute;right:24px;top:28px;display:flex;align-items:center;gap:10px;font-family:"Noto Serif JP",serif;font-size:40px;color:var(--green);font-weight:700;white-space:nowrap}
.nav{position:absolute;left:0;top:104px;width:1200px;height:44px;border-bottom:2px solid var(--line);display:flex;justify-content:space-between;padding:0 72px}
.nav a{color:var(--ink);text-decoration:none;font-size:17px;padding:8px 18px}
/* hero */
.hero{top:160px;height:352px;background:linear-gradient(90deg,#fafafa 0%,#f2f2f2 45%,#e6ece0 60%,#4e7f2e 85%,#2d5a1c 100%)}
.hero-photo{position:absolute;right:0;top:0;width:620px;height:352px;background:linear-gradient(90deg,rgba(250,250,250,0) 0%,rgba(90,130,60,.35) 40%,rgba(40,80,30,.7) 100%)}
.hero h1{position:absolute;left:96px;top:160px;font-family:"Noto Serif JP",serif;font-weight:400;font-size:48px;color:#222}
.hero p{position:absolute;left:116px;top:232px;font-family:"Noto Serif JP",serif;color:var(--green-soft);font-size:28px;line-height:1.45}
/* headings */
.heading{position:absolute;left:0;width:1200px;text-align:center;font-size:24px;color:var(--ink)}
.heading::after{content:"";display:block;width:56px;height:3px;background:var(--green);margin:6px auto 0}
/* business */
.banner{position:absolute;overflow:hidden}
.banner-label{position:absolute;left:50%;transform:translateX(-50%);bottom:20px;background:rgba(0,0,0,.45);color:#fff;text-align:center;padding:6px 24px;font-size:22px;line-height:1.3;min-width:320px}
.banner-label small{display:block;font-size:14px}
/* news */
.news{top:1272px;left:72px;width:1056px;border-top:3px solid var(--green)}
.news-row{display:flex;height:35px;align-items:center;border-bottom:1px solid var(--line);font-size:15px}
.news-row time{width:210px;padding-left:24px}
/* info bands */
.band{height:232px}
.band-photo{position:absolute;top:0;height:232px}
.band-body{position:absolute;top:20px;width:420px}
.band-body h3{font-size:24px;font-weight:500;margin-bottom:14px;text-align:center}
.band-body p{font-size:15px;line-height:1.55;margin-bottom:10px}
.btn{display:flex;align-items:center;justify-content:center;gap:14px;background:var(--green);color:#fff;border-radius:8px;font-size:17px;height:32px;text-decoration:none}
/* products */
.product{position:absolute;width:496px}
.product-photo{height:248px;background:radial-gradient(ellipse at 50% 55%,#e2c43a 0%,#c9a92a 18%,#f6f6f6 42%,#fff 70%)}
.product p{font-size:15px;line-height:1.6;margin-top:14px}
.more{position:absolute;left:520px;width:160px;height:32px}
/* column */
.col{position:absolute;width:336px}
.col-photo{height:136px}
.col p{font-size:14px;line-height:1.6;margin-top:12px}
/* access */
.info{position:absolute;width:480px}
.info h3{font-family:"Noto Serif JP",serif;font-size:26px;font-weight:400;border-bottom:1px solid var(--line);padding-bottom:6px;margin-bottom:20px}
.info p{font-family:"Noto Serif JP",serif;font-size:16px;line-height:1.6}
/* footer */
.footer{top:4448px;height:296px;background:var(--bg-soft)}
.footer .brand{position:absolute;left:72px;top:30px;font-size:36px}
.footer-addr{position:absolute;left:152px;top:90px;font-family:"Noto Serif JP",serif;font-size:17px;line-height:1.5}
.footer-links{position:absolute;top:50px;list-style:none;font-size:16px;line-height:1.65}
.footer-links li::before{content:"> "}
.copyright{top:4744px;height:40px;background:var(--green-dark);color:#fff;text-align:center;font-size:13px;line-height:40px}
</style>
</head>
<body>

<header class="section header">
  <div class="brand"><span class="brand-dot"></span>midori-eco</div>
  <div class="tel">
    <svg width="38" height="38" viewBox="0 0 24 24" aria-hidden="true"><rect x="1" y="1" width="22" height="22" rx="3" fill="var(--green)"/><path d="M8 5.5l2 3-1.3 1.5c.9 1.8 2.3 3.2 4.1 4.1l1.5-1.3 3 2-1 2.5c-5.5-.3-10.4-5.2-10.7-10.7z" fill="#fff"/></svg>
    0120-555-310
  </div>
  <nav class="nav">
    <a>会社情報</a><a>事業紹介</a><a>商品情報</a><a>環境保護方針</a><a>採用情報</a><a>お問い合わせ</a>
  </nav>
</header>

<section class="section hero">
  <div class="hero-photo" role="img" aria-label="緑の葉に包まれたスーツ姿のビジネスパーソン"></div>
  <h1>コピーサンプル</h1>
  <p>サンプルサンプルサンプルサンプルサンプル<br>サンプルサンプルサンプルサンプルサンプル</p>
</section>

<h2 class="heading" style="top:564px">事業紹介</h2>
<div class="banner" style="left:72px;top:632px;width:1056px;height:240px;background:linear-gradient(90deg,#3f6b2a,#cfd8c4 45%,#e9ece4 60%,#5c7f3a)" role="img" aria-label="苔の上に置かれたガラスの地球と植物">
  <div class="banner-label">環境事業<small>Environmental business</small></div>
</div>
<div class="banner" style="left:72px;top:896px;width:512px;height:240px;background:linear-gradient(180deg,#4f86c9,#9cc0e6 55%,#8b7a60)" role="img" aria-label="青空の下の建設クレーン">
  <div class="banner-label" style="min-width:260px">建設事業<small>Construction business</small></div>
</div>
<div class="banner" style="left:616px;top:896px;width:512px;height:240px;background:linear-gradient(180deg,#7fa8d8,#dfe7ef 55%,#9a9a9a)" role="img" aria-label="道路を走る白い大型トラック">
  <div class="banner-label" style="min-width:260px">運搬事業<small>Transportation business</small></div>
</div>

<h2 class="heading" style="top:1188px">News</h2>
<div class="section news">
  <div class="news-row"><time>2019/10/8</time>サンプルサンプルサンプルサンプルサンプルサンプルサンプルサンプルサンプルサンプル</div>
  <div class="news-row"><time>2019/10/8</time>サンプルサンプルサンプルサンプルサンプルサンプルサンプルサンプルサンプルサンプル</div>
  <div class="news-row"><time>2019/10/8</time>サンプルサンプルサンプルサンプルサンプルサンプルサンプルサンプルサンプルサンプル</div>
  <div class="news-row"><time>2019/10/8</time>サンプルサンプルサンプルサンプルサンプルサンプルサンプルサンプルサンプルサンプル</div>
  <div class="news-row"><time>2019/10/8</time>サンプルサンプルサンプルサンプルサンプルサンプルサンプルサンプルサンプルサンプル</div>
  <div class="news-row"><time>2019/10/8</time>サンプルサンプルサンプルサンプルサンプルサンプルサンプルサンプルサンプルサンプル</div>
  <div class="news-row"><time>2019/10/8</time>サンプルサンプルサンプルサンプルサンプルサンプルサンプルサンプルサンプルサンプル</div>
  <div class="news-row"><time>2019/10/8</time>サンプルサンプルサンプルサンプルサンプルサンプルサンプルサンプルサンプルサンプル</div>
</div>

<section class="section band" style="top:1592px">
  <div class="band-photo" style="left:0;width:660px;background:linear-gradient(90deg,#1c3f7a,#3d74b8 50%,#a9c6e6 80%,rgba(255,255,255,0))" role="img" aria-label="青いガラス張りのオフィスビル"></div>
  <div class="band-body" style="left:690px">
    <h3>会社情報</h3>
    <p>サンプルテキストサンプルテキストサンプルテキストサンプルテキストサンプルテキストサンプルテキストサンプルテキストサンプルテキスト</p>
    <a class="btn">会社情報 <span>➜</span></a>
  </div>
</section>
<section class="section band" style="top:1832px">
  <div class="band-photo" style="left:540px;width:660px;background:linear-gradient(90deg,rgba(255,255,255,0),#d8d8d8 25%,#3a3a3a 45%,#e8e8e8 65%,#2e2e2e 85%,#cfcfcf)" role="img" aria-label="腕を組んで並ぶスーツ姿のビジネスチーム"></div>
  <div class="band-body" style="left:96px;top:12px;background:rgba(255,255,255,.9);padding:10px">
    <h3>採用情報</h3>
    <p>サンプルテキストサンプルテキストサンプルテキストサンプルテキストサンプルテキストサンプルテキストサンプルテキストサンプルテキスト</p>
    <a class="btn">会社情報 <span>➜</span></a>
  </div>
</section>
<section class="section band" style="top:2072px">
  <div class="band-photo" style="left:0;width:660px;background:linear-gradient(90deg,#3a2a1c,#6b4e32 35%,#8aa854 55%,#d6e2c2 80%,rgba(255,255,255,0))" role="img" aria-label="土から芽吹く若葉を包む両手"></div>
  <div class="band-body" style="left:690px">
    <h3>環境保護活動</h3>
    <p>サンプルテキストサンプルテキストサンプルテキストサンプルテキストサンプルテキストサンプルテキストサンプルテキストサンプルテキスト</p>
    <a class="btn">会社情報 <span>➜</span></a>
  </div>
</section>

<h2 class="heading" style="top:2348px">商品情報</h2>
<div class="product" style="left:88px;top:2424px">
  <div class="product-photo" role="img" aria-label="黄色い油圧ショベル"></div>
  <p>サンプルサンプルサンプルサンプルサンプルサンプルサンプルサンプルサンプルサンプル<br>サンプルサンプルサンプル<br>サンプルサンプルサンプルサンプルサンプル</p>
</div>
<div class="product" style="left:616px;top:2424px">
  <div class="product-photo" role="img" aria-label="黄色い油圧ショベル"></div>
  <p>サンプルサンプルサンプルサンプルサンプルサンプルサンプルサンプルサンプルサンプル<br>サンプルサンプルサンプル<br>サンプルサンプルサンプルサンプルサンプル</p>
</div>
<div class="product" style="left:88px;top:2824px">
  <div class="product-photo" role="img" aria-label="黄色い油圧ショベル"></div>
  <p>サンプルサンプルサンプルサンプルサンプルサンプルサンプルサンプルサンプルサンプル<br>サンプルサンプルサンプル<br>サンプルサンプルサンプルサンプルサンプル</p>
</div>
<div class="product" style="left:616px;top:2824px">
  <div class="product-photo" role="img" aria-label="黄色い油圧ショベル"></div>
  <p>サンプルサンプルサンプルサンプルサンプルサンプルサンプルサンプルサンプルサンプル<br>サンプルサンプルサンプル<br>サンプルサンプルサンプルサンプルサンプル</p>
</div>
<a class="btn more" style="top:3264px">さらに表示</a>

<h2 class="heading" style="top:3340px">コラム</h2>
<div class="col" style="left:72px;top:3400px">
  <div class="col-photo" style="background:linear-gradient(135deg,#6d88a8,#c9b08a 50%,#8a6a4a)" role="img" aria-label="工場の作業現場"></div>
  <p>サンプルサンプルサンプルサンプルサンプルサンプルサンプルサンプルサンプル<br>サンプルサンプルサンプルサンプルサンプルサンプル</p>
</div>
<div class="col" style="left:432px;top:3400px">
  <div class="col-photo" style="background:linear-gradient(135deg,#3c5a7a,#d1a640 45%,#6a5a48)" role="img" aria-label="重機が並ぶ作業場"></div>
  <p>サンプルサンプルサンプルサンプルサンプルサンプルサンプルサンプルサンプル<br>サンプルサンプルサンプルサンプルサンプルサンプル</p>
</div>
<div class="col" style="left:792px;top:3400px">
  <div class="col-photo" style="background:linear-gradient(135deg,#a9c7de,#6f8fa8 50%,#b8c6cf)" role="img" aria-label="リサイクル施設の内部"></div>
  <p>サンプルサンプルサンプルサンプルサンプルサンプルサンプルサンプルサンプル<br>サンプルサンプルサンプルサンプルサンプルサンプル</p>
</div>
<a class="btn more" style="top:3736px">さらに表示</a>

<div class="info" style="left:96px;top:3808px">
  <h3>アクセス</h3>
  <p>サンプルテキストサンプルテキストサンプルテキストxxにお越しください。</p>
  <p style="margin-top:14px;padding-left:16px">〒999-9999<br>東京都x x区x x x 9-999-99<br>TEL：0120-555-310<br>FAX：0120-555-311</p>
</div>
<div class="info" style="left:632px;top:3808px">
  <h3>お問い合わせ</h3>
  <p>サンプルテキストサンプルテキストサンプルテキストサンプルテキストサンプルテキストサンプルテキスト<br>お気軽にお問い合わせください。</p>
  <a class="btn" style="width:360px;margin:28px auto 0;height:48px">お問い合わせ <span>➜</span></a>
</div>

<div class="section" style="top:4144px;height:296px;background:linear-gradient(120deg,#e4e9df 0%,#cfdcc4 35%,#eceeea 55%,#c6d6e4 75%,#dfe6d6 100%)" role="img" aria-label="所在地周辺の地図"></div>

<footer class="section footer">
  <div class="brand"><span class="brand-dot"></span>midori-eco</div>
  <div class="footer-addr">〒999-9999<br>東京都x x区x x x 9-999-99<br>TEL：0120-555-310<br>FAX：0120-555-311</div>
  <ul class="footer-links" style="left:672px">
    <li>会社情報</li><li>採用情報</li><li>事業紹介</li><li>商品情報</li><li>環境保護方針</li>
  </ul>
  <ul class="footer-links" style="left:896px">
    <li>お問い合わせ</li><li>プライバシーポリシー</li><li>サイトマップ</li>
  </ul>
</footer>
<div class="section copyright">© 2019 midori-eco - All rights reserved</div>

</body>
</html>
```